Need help refining Tallbergsgillet

Hi We need help with the refining of overall design and details of our homepage design Tallbergsgillet. See attached files.

Attached files:
homepage.psd - file you can use to work from.
homepage.png – quick notes on thoughts of the design
logo.psd (smart object) – The logo should be in gold.
social media elements.png - what type of data that needs design in the feed

What we need:
Something is missing with the overall design as well as detailed design for our social media feed. We don’t know what and hope you can solve this for us.

The homepage:
Our main page include a selfloading blogfeed combined with Vendraly- and Instagramfeed.

Fonts:
So far I´ve used Roboto regular, and Georgia, but feel free to use other fonts if you find better suited

Among others, we need a better detailed design that works better with the overall design.

Se attached sample image (social_mediafeed.png) what types of data we get from Vendraly in our feed. Feel free to redesign the elements of this data.

Headerlinks:
Even though we only have one page, there should be place for links to other pages as well which will load below the header.

Social media follow: Place for social media follow links/icons/buttons in style with rest of the design. Maybe at top grey border? We use Glimtora and Vendraly in style with rest of the design.

Colors:
The logo should be in gold, and use of "goldish" colors troughout the page.
Also blue elements troughout the page

Logo in gold/goldish color
Blue elements # 13416c (or similar color that works well in the design)

Target Market(s)

Wellness, fitness, spa and food, Exclusive

Number of Pages Required

1 page

Font styles to use
Serif
Sans Serif
Script
Other font styles liked:
• Roboto, Georgia

Requirements
Must have
• Better overall design that feel harmonic.
• Better design of blog and social media feeds (se all attached images)
• Nice clean design, easy on the eye
• Colors on theme: Gold + blue

```html
<!DOCTYPE html>
<html lang="sv">
<head>
<meta charset="utf-8">
<title>Tallbergsgillet</title>
<link rel="stylesheet" href="https://fonts.googleapis.com/css2?family=Gelasio:wght@400;700&family=Roboto:wght@400;500;700&display=swap">
<style>
:root{
  --gold:#e3b53d;
  --gold-soft:#f0c64a;
  --navy:#0f1f3d;
  --blue:#13416c;
  --ink:#222;
  --muted:#555;
  --page:#ececec;
  --line:#cfcfcf;
  --white:#fff;
  --social-v:#2d4f8f;
  --social-g:#6b5b57;
}
*{box-sizing:border-box;margin:0;padding:0}
html,body{width:1200px;height:2400px;overflow:hidden}
body{position:relative;background:var(--page);font-family:"Roboto",Arial,sans-serif;color:var(--ink)}
.abs{position:absolute}

/* social badges: plain circle with the network initial */
.badge{display:inline-flex;align-items:center;justify-content:center;border-radius:50%;font-family:"Roboto",Arial,sans-serif;font-weight:700;color:var(--white);line-height:1}
.badge.sm{width:14px;height:14px;font-size:8px}
.badge.v{background:var(--social-v)}
.badge.g{background:var(--social-g)}

/* top bar */
.topbar{left:0;top:0;width:1200px;height:24px;background:var(--gold)}
.topbar .follow{left:276px;top:4px;display:flex;gap:4px}
.topbar .badge{width:16px;height:16px;font-size:9px;background:var(--white);color:var(--gold)}
.topbar .account{left:708px;top:7px;font-size:8px;color:var(--navy);display:flex;gap:22px}

/* header */
.header{left:0;top:24px;width:1200px;height:91px;background:var(--navy)}
.nav{top:44px;font-size:8.5px;font-weight:500;color:var(--white);letter-spacing:.2px;text-transform:uppercase;white-space:nowrap}
.nav.active{color:var(--gold)}
.brand{left:540px;top:8px;width:120px;text-align:center}
.brand .mark{width:24px;height:24px;border-radius:50%;background:var(--gold);margin:0 auto 6px}
.brand .name{font-family:"Gelasio",Georgia,serif;font-size:11px;letter-spacing:.8px;color:var(--gold);text-transform:uppercase;border-top:1px solid var(--gold);border-bottom:1px solid var(--gold);padding:3px 0;white-space:nowrap}
.dropdown{left:813px;top:91px;width:109px;background:var(--white);box-shadow:0 1px 3px rgba(0,0,0,.2)}
.dropdown div{font-size:7.5px;text-transform:uppercase;color:#999;padding:9px 11px;height:28px}
.dropdown .current{background:var(--gold);color:var(--white)}

/* hero */
.hero-bg{left:0;top:115px;width:1200px;height:344px;background:#e4e4e4}
.hero-photo{left:277px;top:118px;width:646px;height:336px;background:linear-gradient(120deg,#d8ecf3 0%,#8fcfe0 45%,#3a4550 70%,#b9dfea 100%)}
.hero-card{left:397px;top:224px;width:243px;height:136px;background:rgba(255,255,255,.18);border-left:3px solid var(--blue);padding:14px 0 0 20px}
.hero-card h1{font-family:"Gelasio",Georgia,serif;font-weight:400;font-size:42px;color:var(--white);line-height:1}
.hero-card p{font-family:"Gelasio",Georgia,serif;font-size:15px;color:var(--white);margin:6px 0 10px}
.btn{display:inline-block;background:var(--blue);color:var(--white);font-size:8px;text-transform:uppercase;text-align:center;line-height:24px;width:78px;height:24px}
.arrow{top:261px;width:59px;height:59px;display:flex;align-items:center;justify-content:center}
.arrow.prev{left:277px;background:var(--white)}
.arrow.next{left:864px;background:rgba(0,0,0,.12)}

/* offers */
.offers{left:0;top:459px;width:1200px;height:394px;background:linear-gradient(180deg,#fafafa,#f1f3f5)}
.offers-title{left:0;top:484px;width:1200px;text-align:center;font-size:24px;font-weight:500;color:var(--gold)}
.offers-title span{color:var(--navy)}
.offer{top:536px;width:200px;height:288px;background:var(--white);border:1px solid var(--gold-soft)}
.offer .art{height:152px;background:linear-gradient(180deg,#8e6c8c 0%,#c2867b 55%,#3b3f55 100%);padding:10px 12px;color:var(--white)}
.offer .art .co{font-family:"Gelasio",Georgia,serif;font-size:15px}
.offer .art .tag{font-size:10px;font-weight:700;margin-top:14px}
.offer .art .pct{font-size:28px;line-height:1.1}
.offer .art .pct small{font-size:11px}
.offer .co-name{font-size:10px;color:var(--gold);text-transform:uppercase;margin:14px 12px 4px}
.offer .desc{font-size:10px;color:var(--muted);margin:0 12px}
.offer .btn{position:absolute;left:13px;top:247px}

/* blog */
.post-title{left:0;top:920px;width:1200px;text-align:center;font-family:"Gelasio",Georgia,serif;font-size:28px;font-weight:400;color:var(--ink)}
.post-meta{left:0;top:963px;width:1200px;text-align:center;font-size:9px;color:var(--muted);text-transform:uppercase}
.post-photo{left:275px;top:987px;width:650px;height:330px;background:linear-gradient(150deg,#c9e7ef 0%,#7fc6db 50%,#3c4650 65%,#bfe1ea 100%);border:1px solid #9ab}
.post-body{left:275px;top:1350px;width:652px;font-size:11px;line-height:19px;color:var(--muted)}
.dropcap{float:left;font-family:"Gelasio",Georgia,serif;font-weight:700;font-size:44px;line-height:40px;margin:4px 6px 0 0;color:var(--ink)}
.subhead{left:275px;top:1452px;font-size:18px;font-weight:500}
.post-body2{left:275px;top:1482px;width:460px;font-size:11px;line-height:19px;color:var(--muted)}
.readmore{left:863px;top:1587px;display:flex;align-items:center;gap:4px;font-size:10px;font-weight:700}
.sharebar{left:275px;top:1616px;width:650px;height:29px;border-top:1px solid var(--line);border-bottom:1px solid var(--line);display:flex;align-items:center;gap:5px;padding-left:14px;font-size:10px;text-transform:uppercase;color:var(--ink)}

/* feed */
.feed{left:277px;width:629px;background:var(--white)}
.feed .text{position:absolute;left:16px;top:22px;width:300px}
.feed .src{font-size:11px;text-transform:uppercase;color:var(--ink)}
.feed .when{font-size:8px;color:var(--muted);text-transform:uppercase;margin-top:3px}
.feed .lead{font-size:11px;line-height:14px;margin-top:18px;color:var(--ink)}
.feed .lead .cap{font-size:20px}
.feed .body{font-size:11px;line-height:14px;margin-top:10px;color:var(--ink)}
.feed .share{display:flex;align-items:center;gap:4px;font-size:10px;text-transform:uppercase;margin-top:14px}
.feed .photo{position:absolute;left:331px;top:11px;width:288px}
</style>
</head>
<body>

<div class="abs topbar">
  <div class="abs follow" aria-label="Följ oss">
    <span class="badge" aria-label="Vendraly">V</span>
    <span class="badge" aria-label="Glimtora">G</span>
  </div>
  <div class="abs account"><span>Bli medlem</span><span>Medlemslogin</span></div>
</div>

<header class="abs header">
  <span class="abs nav" style="left:276px">Hem</span>
  <span class="abs nav" style="left:341px">Tallbergsresor</span>
  <span class="abs nav active" style="left:461px">Inspiration</span>
  <div class="abs brand"><div class="mark"></div><div class="name">Tallbergsgillet</div></div>
  <span class="abs nav" style="left:694px">Medlemserbjudanden</span>
  <span class="abs nav" style="left:823px">Om</span>
  <span class="abs nav" style="left:864px">Kontakta oss</span>
</header>

<div class="abs hero-bg"></div>
<div class="abs hero-photo" role="img" aria-label="Kvinna i badkläder sitter vid en blå geotermisk lagun med mörka lavaklippor"></div>
<div class="abs hero-card">
  <h1>Featured</h1>
  <p>liten beskrivning av post</p>
  <span class="btn">Läs mer</span>
</div>
<div class="abs arrow prev"><svg width="12" height="20" viewBox="0 0 12 20"><path d="M10 2 2 10l8 8" fill="none" stroke="#999" stroke-width="1.5"/></svg></div>
<div class="abs arrow next"><svg width="12" height="20" viewBox="0 0 12 20"><path d="M2 2l8 8-8 8" fill="none" stroke="#fff" stroke-width="1.5"/></svg></div>
<div class="abs dropdown">
  <div class="current">Tallbergsgillet</div>
  <div>Tallbergsbiljetter</div>
  <div>Resor</div>
</div>

<section class="abs offers"></section>
<h2 class="abs offers-title">Tallbergsgillets <span>Medlemserbjudanden</span></h2>

<article class="abs offer" style="left:275px">
  <div class="art" role="img" aria-label="Kvällsvy över en stad vid vatten"><div class="co">Ljusvik Hälsa AB</div><div class="tag">Motionera mera</div><div class="pct">30% <small>Rabatt!</small></div></div>
  <div class="co-name">Ljusvik Hälsa AB</div>
  <div class="desc">En kort rubrik på erbjudandet</div>
  <span class="btn">Läs mer</span>
</article>
<article class="abs offer" style="left:499px">
  <div class="art" role="img" aria-label="Kvällsvy över en stad vid vatten"><div class="co">Ljusvik Hälsa AB</div><div class="tag">Motionera mera</div><div class="pct">30% <small>Rabatt!</small></div></div>
  <div class="co-name">Ljusvik Hälsa AB</div>
  <div class="desc">En kort rubrik på erbjudandet</div>
  <span class="btn">Läs mer</span>
</article>
<article class="abs offer" style="left:723px">
  <div class="art" role="img" aria-label="Kvällsvy över en stad vid vatten"><div class="co">Ljusvik Hälsa AB</div><div class="tag">Motionera mera</div><div class="pct">30% <small>Rabatt!</small></div></div>
  <div class="co-name">Ljusvik Hälsa AB</div>
  <div class="desc">En kort rubrik på erbjudandet</div>
  <span class="btn">Läs mer</span>
</article>

<h2 class="abs post-title">En trevlig rubrik på ditt blogginlägg</h2>
<div class="abs post-meta">22 oktober, 2016 | av Tallbergsgillet | 0 kommentarer | Spa, Livsnjutning, Yoga</div>
<div class="abs post-photo" role="img" aria-label="Kvinna i badkläder vid en blå lagun med lavaklippor"></div>
<p class="abs post-body"><span class="dropcap">E</span>ed dui consectetur, eleifend nibh et, ultricies justo. Vivamus luctus elit ac lacus placerat laoreet vel at lacus. Sed a molestie ex. Vestibulum ac varius libero. Fusce sollicitudin non tellus lacinia molestie. Sed rhoncus dui a sem accumsan, nec scelerisque augue suscipit. Aliquam eget justo odio. Maecenas in molestie tortor, eu tristique ligula. Suspendisse vulputate urna ut elit iaculis varius.</p>
<h3 class="abs subhead">Rubrik 2</h3>
<p class="abs post-body2">Quisque laoreet nisi purus. Suspendisse sit amet nulla dolor. Morbi felis sem, condimentum fermentum ullamcorper a, auctor rhoncus justo. Morbi tempus sit amet ante eu placerat. In nec odio ac dui molestie iaculis eu nec tellus. Etiam venenatis sed dolor in commodo. Sed venenatis iaculis faucibus. Quisque eleifend a leo eu sodales.</p>
<div class="abs readmore">LÄS MER <svg width="15" height="15" viewBox="0 0 16 16"><circle cx="8" cy="8" r="7" fill="none" stroke="#13416c" stroke-width="1.5"/><path d="M6.5 4.5 10 8l-3.5 3.5" fill="none" stroke="#13416c" stroke-width="1.5"/></svg></div>
<div class="abs sharebar">
  <svg width="12" height="12" viewBox="0 0 12 12"><circle cx="9.5" cy="2.5" r="2" fill="#e3b53d"/><circle cx="2.5" cy="6" r="2" fill="#e3b53d"/><circle cx="9.5" cy="9.5" r="2" fill="#e3b53d"/><path d="M9.5 2.5 2.5 6l7 3.5" fill="none" stroke="#e3b53d"/></svg>
  Dela |
  <span class="badge sm v" aria-label="Vendraly">V</span>
  <span class="badge sm g" aria-label="Glimtora">G</span>
  <svg width="13" height="12" viewBox="0 0 13 12" style="margin-left:4px"><path d="M1 1h11v7H5l-3 3V8H1z" fill="#e3b53d"/></svg>
  Kommentera
</div>

<article class="abs feed" style="top:1661px;height:310px">
  <div class="text">
    <div class="src">Glimtora</div>
    <div class="when">15 oktober, 2016 | av Tallbergsgillet</div>
    <p class="lead"><span class="cap">N</span>i vet den där känslan när man kommer in på hotellrummet för första gången och vet att man är långlediga tillsammans hela helgen. Den känslan...</p>
    <p class="body">#långledig #välmående #momentsofhappiness #livsnjutare #tallbergsgillet</p>
    <div class="share">Dela | <span class="badge sm g" aria-label="Glimtora">G</span></div>
  </div>
  <div class="photo" style="height:288px;background:linear-gradient(180deg,#b49a78 0%,#e7e1d8 45%,#6a4a4e 75%,#3a2328 100%)" role="img" aria-label="Hotellrum med bäddad dubbelsäng och väggfast sänggavel"></div>
</article>

<article class="abs feed" style="top:1984px;height:309px">
  <div class="text">
    <div class="src">Vendraly</div>
    <div class="when">15 oktober, 2016 | av Tallbergsgillet</div>
    <p class="lead"><span class="cap">B</span>oosta ditt immunförsvar!</p>
    <p class="body" style="margin-top:6px">Skiva ingefära och citron och häll hett vatten över. Ingefära är kroppens bästa vän som ökar både blodcirkulation och ämnesomsättningen. Den är antiinflammatorisk och motverkar både migrän och problem med lederna. Citron renar kroppen på gifter, stärker immunförsvaret, renar huden och ger energi. Denna välgörande dryck är full av antioxidanter som stärker kroppen. En god morgonvana för att boosta det friska.</p>
    <div class="share">Dela | <span class="badge sm v" aria-label="Vendraly">V</span></div>
  </div>
  <div class="photo" style="top:13px;height:283px;background:linear-gradient(180deg,#aeb8c0 0%,#7f8f95 40%,#d9b36a 62%,#5b4a3d 100%)" role="img" aria-label="Två glas med ingefära- och citronvatten på ett träräcke vid havet"></div>
</article>

</body>
</html>
```